The Gemstone Craft Studio Sales Business Card

The goal of this project is to create a interactive & effective business card design for SALES purposes with the intention to get customer on to our website and make a purchase or contact us about a product or service.
Website: WWW.RINGFORGEHUB.COM
GoogleMyBusiness: https://g.page/RingForgeHUB?gm
Facebook & Instagram: @THEGEMSTONECRAFTSTUDIO
Phone # & Text Message & Whatsapp Message: +1(555) 418-0293
Email: HELLO@RINGFORGEHUB.COM
Location: 4872 Brambleton Avenue Suite 512 Cedarvale, PA
(It would be necessary to have the appropriate ticker/icon for each social media platform as well as the location ticker and phone / messaging icons instead of spelling the words out.)
It is important to have the company logo and details but with an emphasis toward website. Feel free to also completely make one design your way and completely custom as you feel best.
The Gemstone Craft Studio is a Provider of Luxury Goods & Services such as: Custom Jewelry Design, Jewelry Repairs & Cleaning, Designer Jewelry, Luxury Gifts, 24 Karat Gold, 22 Karat Gold Jewelry, Diamond Jewelry, Insured Jewelry Appraisals, Loose Gemstones & Diamonds, Supporting Sustainability
Target Market(s)
People looking to invest in precious metals and gemstones as well as people looking to find a gift for a loved one for a special occasion. Customers looking to Custom Design Jewelry.
Contact Information for Business Card
Font styles to use
Other font styles liked:
- w.e you want
Colors
Designer to choose colors to be used in the design.
Requirements
Must have
- Website: WWW.RINGFORGEHUB.COM
- GoogleMyBusiness: https://g.page/RingForgeHUB?gm
- Facebook & Instagram: @THEGEMSTONECRAFTSTUDIO
- Phone # & Text Message & Whatsapp Message: +1(555) 418-0293
- Email: HELLO@RINGFORGEHUB.COM
- Location: 4872 Brambleton Avenue Suite 512 Cedarvale, PA
- (It would be necessary to have the appropriate ticker/icon for each social media platform as well as the location ticker and phone / messaging icons instead of spelling the words out.)
- It is important to have the company logo and details but with an emphasis toward website. Feel free to also completely make one design your way and completely custom as you feel best.
Nice to have
- The Gemstone Craft Studio is a Provider of Luxury Goods & Services such as: Custom Jewelry Design, Jewelry Repairs & Cleaning, Designer Jewelry, Luxury Gifts, 24 Karat Gold, 22 Karat Gold Jewelry, Diamond Jewelry, Insured Jewelry Appraisals, Loose Gemstones & Diamonds, Supporting Sustainability

```html
<!DOCTYPE html>
<html lang="en">
<head>
<meta charset="utf-8">
<title>The Gemstone Craft Studio – Business Card</title>
<link rel="stylesheet" href="https://fonts.googleapis.com/css2?family=Cinzel:wght@700&family=Roboto:wght@400;700&display=swap">
<style>
  :root {
    --backdrop: #2f241f;
    --card-black: #0a0a0a;
    --card-white: #ffffff;
    --brand-red: #e31e2d;
    --brand-gold: #f4c237;
    --text-red: #e31e2d;
  }
  * { box-sizing: border-box; margin: 0; padding: 0; }
  html, body { width: 1200px; height: 716px; overflow: hidden; }
  body {
    background: var(--backdrop);
    font-family: "Roboto", Arial, sans-serif;
    position: relative;
  }
  .card {
    position: absolute;
    width: 520px;
    height: 297px;
    top: 210px;
    border-radius: 3px;
    overflow: hidden;
  }
  /* ---------- Front ---------- */
  .card-front { left: 60px; background: var(--card-black); }
  .front-shape { position: absolute; inset: 0; }
  .front-brand {
    position: absolute;
    left: 200px;
    top: 62px;
    width: 290px;
    font-family: "Cinzel", Georgia, serif;
    font-weight: 700;
    font-size: 30px;
    line-height: 1.1;
    color: var(--brand-red);
    letter-spacing: 0.5px;
  }
  /* ---------- Back ---------- */
  .card-back { left: 620px; background: var(--card-white); }
  .person { position: absolute; left: 40px; top: 64px; }
  .person-name { font-weight: 700; font-size: 18px; color: var(--brand-gold); }
  .person-role { font-size: 9px; color: var(--text-red); margin-top: 2px; }
  .divider {
    position: absolute; left: 40px; top: 112px;
    width: 445px; height: 1.5px; background: var(--brand-red);
  }
  .back-brand {
    position: absolute; right: 36px; top: 44px;
    width: 200px; text-align: center;
    font-family: "Cinzel", Georgia, serif; font-weight: 700;
    font-size: 19px; line-height: 1.1; color: var(--brand-red);
  }
  .contacts { position: absolute; left: 40px; top: 124px; list-style: none; }
  .contacts li {
    display: flex; align-items: center; gap: 6px;
    font-size: 10.5px; color: var(--text-red); height: 16px;
  }
  .contacts svg { width: 10px; height: 10px; flex: none; }
  .icon-pair { display: flex; gap: 2px; }
  .address {
    position: absolute; left: 318px; top: 178px;
    font-size: 11px; line-height: 1.35; color: var(--text-red);
    font-style: normal;
  }
  .back-footer { position: absolute; left: 0; bottom: 0; width: 520px; height: 70px; }
  .website {
    position: absolute; right: 22px; bottom: 9px;
    font-size: 12px; color: #fff; letter-spacing: 0.3px;
  }
</style>
</head>
<body>

  <section class="card card-front" aria-label="Business card front">
    <svg class="front-shape" viewBox="0 0 520 297" aria-hidden="true">
      <polygon points="0,0 170,0 120,297 0,297" fill="var(--brand-red)"/>
    </svg>
    <h1 class="front-brand">The Gemstone Craft Studio</h1>
  </section>

  <section class="card card-back" aria-label="Business card back">
    <div class="person">
      <p class="person-name">Marcus Ellery</p>
      <p class="person-role">Manager</p>
    </div>

    <p class="back-brand">The Gemstone Craft Studio</p>
    <div class="divider"></div>

    <ul class="contacts">
      <li>
        <svg viewBox="0 0 10 10" aria-hidden="true"><path d="M2 1 L4 1 L4.6 3.2 L3.5 4 Q4.6 6 6 6.6 L6.8 5.4 L9 6 L9 8 Q8.5 9 7 9 Q1 8 1 2.5 Q1 1.5 2 1Z" fill="var(--brand-gold)"/></svg>
        +1(555) 418-0293
      </li>
      <li>
        <svg viewBox="0 0 10 10" aria-hidden="true"><rect x="0.5" y="2" width="9" height="6.5" rx="1" fill="var(--brand-gold)"/><path d="M1 2.5 L5 5.5 L9 2.5" stroke="#fff" stroke-width="0.8" fill="none"/></svg>
        HELLO@RINGFORGEHUB.COM
      </li>
      <li>
        <svg viewBox="0 0 10 10" aria-hidden="true"><circle cx="5" cy="5" r="4.5" fill="var(--brand-gold)"/></svg>
        g.page/RingForgeHUB?gm
      </li>
      <li>
        <span class="icon-pair">
          <svg viewBox="0 0 10 10" aria-hidden="true"><rect x="0.5" y="0.5" width="9" height="9" rx="1.5" fill="var(--brand-gold)"/></svg>
          <svg viewBox="0 0 10 10" aria-hidden="true"><rect x="0.5" y="0.5" width="9" height="9" rx="1.5" fill="var(--brand-gold)"/></svg>
        </span>
        @THEGEMSTONECRAFTSTUDIO
      </li>
    </ul>

    <address class="address">
      4872 Brambleton Avenue<br>Suite 512<br>Cedarvale, PA
    </address>

    <svg class="back-footer" viewBox="0 0 520 70" aria-hidden="true">
      <path d="M0 44 L240 44 Q252 44 258 40" stroke="var(--brand-gold)" stroke-width="2.5" fill="none"/>
      <path d="M0 60 L255 60 Q265 60 272 48 Q278 38 292 38 L520 38 L520 70 L0 70 Z" fill="var(--brand-red)"/>
    </svg>
    <p class="website">WWW.RINGFORGEHUB.COM</p>
  </section>

</body>
</html>
```